Lumo Vance IT company Soho london Stationary

We've just had a new logo designed on Gallow Pier and we now need some Stationary to go with it.
We're a small IT support firm supporting Design companies in Soho London. Most of our clients work on Vorls and a relatively creative so we want a relatively informal design on our stationary to reflect this.
We'd like to stick with the green in the logo but we're not adverse to adding another few colours to the palette.
Please see the attached file for our logo and not our website.

It Company

```html
<!DOCTYPE html>
<html lang="en">
<head>
<meta charset="utf-8">
<title>Lumo Vance Stationery</title>
<link rel="stylesheet" href="https://fonts.googleapis.com/css2?family=PT+Sans:wght@400;700&display=swap">
<style>
  :root {
    --brand-green: #c5d92d;
    --ink: #2b2b2b;
    --paper: #ffffff;
    --backdrop: #e8e5e1;
    --rule-grey: #c9c9c9;
  }
  * { box-sizing: border-box; margin: 0; padding: 0; }
  html, body { width: 1200px; height: 900px; overflow: hidden; }
  body {
    position: relative;
    background: var(--backdrop);
    font-family: "PT Sans", Arial, sans-serif;
    color: var(--ink);
  }
  .sheet {
    position: absolute;
    background: var(--paper);
    overflow: hidden;
  }
  .wordmark {
    font-weight: 700;
    color: var(--brand-green);
    white-space: nowrap;
    letter-spacing: -0.5px;
  }
  .company-line b { font-weight: 700; }
  .web {
    position: absolute;
    font-size: 9px;
    letter-spacing: 2.2px;
  }
  .green-band {
    position: absolute;
    left: 0; right: 0; bottom: 0;
    background: var(--brand-green);
  }

  /* Letterhead */
  .letterhead { left: 28px; top: 88px; width: 515px; height: 728px; }
  .letterhead .wordmark { position: absolute; left: 37px; top: 36px; font-size: 34px; }
  .letterhead .address {
    position: absolute; left: 307px; top: 34px;
    font-size: 10.5px; line-height: 13px;
    padding-left: 14px;
  }
  .letterhead .address::before {
    content: ""; position: absolute; left: 0; top: -14px;
    width: 2px; height: 78px;
    background: linear-gradient(to bottom, rgba(197,217,45,0), var(--brand-green) 40%, rgba(197,217,45,0));
  }
  .letterhead .web { right: 114px; bottom: 28px; }
  .letterhead .green-band { height: 20px; }

  /* Business cards */
  .card-front { left: 643px; top: 104px; width: 218px; height: 125px; }
  .card-front .accent { position: absolute; left: 0; top: 28px; width: 3px; height: 76px; background: var(--brand-green); }
  .card-front .details { position: absolute; left: 13px; top: 23px; font-size: 5.6px; line-height: 7px; }
  .card-front .details .name { font-size: 7px; line-height: 8px; }
  .card-front .details .gap { height: 5px; }
  .card-front .wordmark { position: absolute; left: 91px; top: 55px; font-size: 19px; }

  .card-back { left: 886px; top: 104px; width: 219px; height: 125px; background: var(--brand-green); }
  .card-back .wordmark { position: absolute; left: 19px; top: 53px; font-size: 18px; color: var(--paper); }
  .card-back .web { left: 39px; top: 76px; font-size: 5.5px; letter-spacing: 1.4px; color: var(--ink); }

  /* Envelope front */
  .envelope-front { left: 580px; top: 265px; width: 590px; height: 257px; }
  .envelope-front .wordmark { position: absolute; left: 24px; top: 26px; font-size: 25px; }
  .envelope-front .address { position: absolute; left: 24px; top: 67px; font-size: 8.5px; line-height: 11px; }
  .envelope-front .web { right: 95px; top: 226px; font-size: 7.5px; letter-spacing: 2px; }
  .envelope-front .green-band { height: 16px; }

  /* Envelope back */
  .envelope-back { left: 580px; top: 540px; width: 590px; height: 257px; }
  .envelope-back svg { position: absolute; left: 0; top: 0; }
  .envelope-back .wordmark { position: absolute; left: 0; right: 0; top: 32px; text-align: center; font-size: 27px; color: var(--paper); }
</style>
</head>
<body>

  <section class="sheet letterhead" aria-label="Letterhead">
    <div class="wordmark">Lumo Vance</div>
    <address class="address" style="font-style:normal">
      <div class="company-line"><b>LumoVance, Inc.</b></div>
      17 Kestrel Lane Suite 4-210<br>
      Marlow, UK 30912
    </address>
    <div class="web">www.lumovance.co.uk</div>
    <div class="green-band"></div>
  </section>

  <section class="sheet card-front" aria-label="Business card front">
    <div class="accent"></div>
    <div class="details">
      <div class="name">Tobin Ashcroft</div>
      <div>Director</div>
      <div class="gap"></div>
      <div><b>LumoVance, Inc.</b></div>
      <div>17 Kestrel Lane</div>
      <div>Suite 4-210</div>
      <div>Marlow, UK 30912</div>
      <div class="gap"></div>
      <div>Ph&nbsp; 020-555-0142</div>
      <div>Fax&nbsp; 020.555.0198</div>
      <div>Em&nbsp; tobin@lumovance.co.uk</div>
      <div class="gap"></div>
      <div>www.lumovance.co.uk</div>
    </div>
    <div class="wordmark">Lumo Vance</div>
  </section>

  <section class="sheet card-back" aria-label="Business card back">
    <div class="wordmark">Lumo Vance</div>
    <div class="web">www.lumovance.co.uk</div>
  </section>

  <section class="sheet envelope-front" aria-label="Envelope front">
    <div class="wordmark">Lumo Vance</div>
    <address class="address" style="font-style:normal">
      <div class="company-line"><b>LumoVance, Inc.</b></div>
      17 Kestrel Lane Suite 4-210<br>
      Marlow, UK 30912
    </address>
    <div class="web">www.lumovance.co.uk</div>
    <div class="green-band"></div>
  </section>

  <section class="sheet envelope-back" aria-label="Envelope back">
    <svg width="590" height="257" viewBox="0 0 590 257" aria-hidden="true">
      <path d="M150 88 L0 232 M440 88 L590 232" stroke="var(--rule-grey)" stroke-width="0.8" fill="none"/>
      <path d="M0 0 H590 V18 Q590 40 566 66 Q552 80 520 82 L310 110 Q295 112 280 110 L70 82 Q38 80 24 66 Q0 40 0 18 Z" fill="var(--brand-green)"/>
    </svg>
    <div class="wordmark">Lumo Vance</div>
  </section>

</body>
</html>
```